Custom Truck shop New Business Card design

double sided business card including my new logo, brand colors and picking a font I attached, clean and modern look. I attached the old card for some reference. and would like to include the picture of the white truck attached. I would also like to have it with one of my employees info as well. (same info except name and title Brin Tolvay Service Writer)

Dale Porvick
Owner

address
48310 E Calloway Ridge Rd S
STE 217
Marsh Hollow, CO 80219

phone 720-555-0184

email dale@brokenspurrigs.example

website brokenspurrgis.example

social @brokenspurrigs

Target Market(s)

men 18-60

Industry/Entity Type

Automotive

Contact Information for Business Card

Dale Porvick Owner address 48310 E Calloway Ridge Rd S STE 217 Marsh Hollow, CO 80219 phone 720-555-0184 email dale@brokenspurrigs.example website brokenspurrgis.example social @brokenspurrigs

Font styles to use
Other font styles liked:
• fonts attached

Requirements
Must have
• new logo, orange #FC68D, Charcoal #333333
Nice to have
• the white truck

```html
<!DOCTYPE html>
<html lang="en">
<head>
<meta charset="utf-8">
<title>Broken Spur Rigs – Business Card</title>
<link rel="stylesheet" href="https://fonts.googleapis.com/css2?family=Jost:wght@500;600;700;800;900&display=swap">
<style>
  :root {
    --orange: #e2693a;
    --charcoal: #333333;
    --card: #f0f0f0;
    --page: #d9d9d9;
    --photo-light: #f2f3f3;
    --photo-mid: #dcdedd;
  }
  * { box-sizing: border-box; margin: 0; padding: 0; }
  html, body { width: 1200px; height: 1200px; overflow: hidden; }
  body {
    background: var(--page);
    font-family: "Jost", sans-serif;
    color: var(--charcoal);
    position: relative;
  }
  .card {
    position: absolute;
    left: 150px;
    width: 900px;
    height: 514px;
    border-radius: 26px;
    background: var(--card);
    overflow: hidden;
    box-shadow: 0 6px 18px rgba(0,0,0,0.18);
  }
  .card--front { top: 66px; }
  .card--back { top: 620px; }

  .truck-photo {
    position: absolute; inset: 0;
    background: linear-gradient(160deg, var(--photo-mid) 0%, var(--photo-light) 45%, var(--photo-mid) 100%);
  }

  .brand {
    position: absolute;
    display: flex;
    flex-direction: column;
    align-items: center;
    gap: 18px;
  }
  .card--front .brand { left: 0; right: 0; top: 150px; }
  .card--back .brand { left: 60px; width: 400px; top: 150px; }
  .brand__dot {
    width: 96px; height: 96px; border-radius: 50%;
    background: var(--orange);
  }
  .brand__name {
    font-weight: 700;
    font-size: 44px;
    letter-spacing: 2px;
    text-transform: uppercase;
    color: var(--charcoal);
    white-space: nowrap;
  }

  .divider {
    position: absolute;
    left: 500px; top: 120px;
    width: 3px; height: 290px;
    background: var(--charcoal);
  }
  .contact {
    position: absolute;
    left: 535px; top: 95px;
    font-weight: 700;
    font-size: 19px;
    line-height: 1.45;
  }
  .contact__name {
    font-weight: 900;
    font-size: 44px;
    color: var(--orange);
    line-height: 1.1;
  }
  .contact__title { font-size: 17px; margin: 4px 0 14px; }
  .contact__address { margin-bottom: 4px; }
  .contact__row { display: flex; align-items: center; gap: 12px; }
  .contact__row svg { width: 20px; height: 20px; flex: none; fill: var(--orange); }
</style>
</head>
<body>

<section class="card card--front">
  <div class="truck-photo" role="img" aria-label="Faded photo of a lifted white pickup truck with large off-road tyres"></div>
  <div class="brand">
    <div class="brand__dot"></div>
    <div class="brand__name">Broken Spur Rigs</div>
  </div>
</section>

<section class="card card--back">
  <div class="brand">
    <div class="brand__dot"></div>
    <div class="brand__name">Broken Spur Rigs</div>
  </div>
  <div class="divider"></div>
  <div class="contact">
    <div class="contact__name">Dale Porvick</div>
    <div class="contact__title">Owner</div>
    <div class="contact__address">48310 E Calloway Ridge Rd S STE 217<br>Marsh Hollow, CO 80219</div>
    <div class="contact__row">
      <svg viewBox="0 0 24 24" aria-hidden="true"><path d="M6.6 10.8a15 15 0 0 0 6.6 6.6l2.2-2.2a1 1 0 0 1 1-.25 11.4 11.4 0 0 0 3.6.57 1 1 0 0 1 1 1V20a1 1 0 0 1-1 1A17 17 0 0 1 3 4a1 1 0 0 1 1-1h3.5a1 1 0 0 1 1 1c0 1.25.2 2.45.57 3.6a1 1 0 0 1-.25 1z"/></svg>
      <span>720-555-0184</span>
    </div>
    <div class="contact__row">
      <svg viewBox="0 0 24 24" aria-hidden="true"><path d="M7 1h10a2 2 0 0 1 2 2v18a2 2 0 0 1-2 2H7a2 2 0 0 1-2-2V3a2 2 0 0 1 2-2zm0 3v14h10V4zm5 15.5a1 1 0 1 0 0 2 1 1 0 0 0 0-2z"/></svg>
      <span>720-555-0162</span>
    </div>
    <div class="contact__row">
      <svg viewBox="0 0 24 24" aria-hidden="true"><path d="M2 5h20v14H2zm2 2v.5l8 5 8-5V7l-8 5z"/></svg>
      <span>dale@brokenspurrigs.example</span>
    </div>
    <div class="contact__row">
      <svg viewBox="0 0 24 24" aria-hidden="true"><path d="M12 2a10 10 0 1 0 0 20 10 10 0 0 0 0-20zm6.9 9h-3a15 15 0 0 0-1.3-5.6A8 8 0 0 1 18.9 11zM12 4c.9 1.2 1.8 3.7 1.9 7h-3.8c.1-3.3 1-5.8 1.9-7zM9.4 5.4A15 15 0 0 0 8.1 11h-3a8 8 0 0 1 4.3-5.6zM5.1 13h3a15 15 0 0 0 1.3 5.6A8 8 0 0 1 5.1 13zM12 20c-.9-1.2-1.8-3.7-1.9-7h3.8c-.1 3.3-1 5.8-1.9 7zm2.6-1.4a15 15 0 0 0 1.3-5.6h3a8 8 0 0 1-4.3 5.6z"/></svg>
      <span>brokenspurrgis.example</span>
    </div>
    <div class="contact__row">
      <svg viewBox="0 0 24 24" aria-hidden="true"><circle cx="12" cy="12" r="6"/></svg>
      <span>@brokenspurrigs</span>
    </div>
  </div>
</section>

</body>
</html>
```